MPD Website Design - very basic

I am looking for preferably an Australian-based web designer to create a website for a new executive services firm. Just looking for a very basic informational site - and hopefully have some guidance on SEO, as that is all new to me.
I have a Capability Statement, which should be all the content needed to create a website.
I did have a logo created (vector files available), and can attach, but I think the background 'navy blue' was too dark in the logo. I have the correct colour code to be used for the background, which is: Blue Color Code : R 18 G 49 B 77 & Hex : #12314D
I've also attached 5 jpg slides, which I had done up to be used as a Linkedin carousel once I launch the business in case they are of use.
Target Market(s)
Small to Medium Business Owners; CEOs of larger organisations and Not-For-Profits
Coding
Coded - Design and coding required
Number of Pages Required
1 page
Look and feel
Each slider illustrates characteristics of the customer's brand and the style your logo design should communicate.

```html
<!DOCTYPE html>
<html lang="en">
<head>
<meta charset="utf-8">
<title>MPD – Executive Services</title>
<link rel="stylesheet" href="https://fonts.googleapis.com/css2?family=Montserrat:wght@300;400;600;700;800&family=Mulish:wght@400;600;700&display=swap">
<style>
  :root{
    --navy:#12314D;
    --navy-deep:#0f2a44;
    --white:#ffffff;
    --ink:#1b1b1b;
    --muted:#4a4a4a;
    --light:#f4f5f7;
    --photo-a:#c9ccd1;
    --photo-b:#e9eaec;
    --black:#050505;
  }
  *{box-sizing:border-box;margin:0;padding:0}
  html,body{width:1200px;height:3296px;overflow:hidden;background:var(--white)}
  body{font-family:'Mulish',sans-serif;color:var(--ink);position:relative}
  section,header,footer{position:absolute;left:0;width:1200px}
  .brand{font-family:'Montserrat',sans-serif;font-weight:800;font-size:40px;letter-spacing:2px;display:flex;align-items:center;gap:12px}
  .brand-dot{width:18px;height:18px;border-radius:50%;display:inline-block}
  .btn{display:inline-block;font-family:'Mulish',sans-serif;font-weight:700;font-size:15px;border-radius:30px;padding:14px 32px}

  /* header */
  .site-header{top:0;height:108px;background:var(--white);box-shadow:0 2px 6px rgba(0,0,0,.06);z-index:2}
  .site-header .brand{position:absolute;left:140px;top:30px;color:var(--navy)}
  .site-header .brand-dot{background:var(--navy)}
  .nav{position:absolute;right:90px;top:30px;display:flex;align-items:center;gap:40px;font-size:16px;font-weight:600;color:var(--ink)}
  .nav .btn{background:var(--navy);color:var(--white);padding:14px 26px}

  /* hero */
  .hero{top:108px;height:662px}
  .hero-photo{position:absolute;left:0;top:0;width:600px;height:662px;background:linear-gradient(135deg,var(--photo-b),var(--photo-a))}
  .hero-panel{position:absolute;left:600px;top:0;width:600px;height:662px;background:var(--navy);padding:150px 0 0 80px;color:var(--white)}
  .hero h1{font-family:'Montserrat',sans-serif;font-weight:700;font-size:58px;line-height:1.02;letter-spacing:1px}
  .hero p{font-size:21px;margin-top:18px;line-height:1.3;max-width:440px}
  .hero .btn{background:var(--white);color:var(--ink);margin-top:36px}

  /* outcome */
  .outcome{top:770px;height:650px}
  .outcome-banner{position:absolute;left:0;top:70px;width:690px;height:180px;fill:var(--navy)}
  .outcome h2{position:absolute;left:140px;top:104px;font-family:'Montserrat',sans-serif;font-size:48px;line-height:1.1;color:var(--white);font-weight:300}
  .outcome h2 strong{font-weight:700;display:block}
  .outcome-copy{position:absolute;left:140px;top:290px;width:480px;font-size:17px;line-height:1.55;color:var(--ink)}
  .outcome-copy p+p{margin-top:26px}
  .outcome .btn{position:absolute;left:140px;top:490px;background:var(--navy);color:var(--white)}
  .outcome-photo{position:absolute;left:680px;top:50px;width:480px;height:550px}

  /* how we work */
  .how{top:1420px;height:540px;background:var(--navy);color:var(--white);text-align:center}
  .how h2{font-family:'Montserrat',sans-serif;font-weight:700;font-size:50px;margin-top:78px;letter-spacing:1px}
  .how .lead{font-size:19px;margin-top:6px}
  .steps{position:absolute;left:60px;top:232px;width:1080px;display:flex;justify-content:space-between}
  .step{width:196px;height:180px;background:var(--white);color:var(--ink);padding:70px 14px 0;position:relative}
  .step-num{position:absolute;left:20px;top:-14px;width:70px;height:70px;border-radius:50%;background:var(--navy-deep);border:4px solid var(--white);color:var(--white);font-family:'Montserrat',sans-serif;font-size:32px;font-weight:600;line-height:62px}
  .step h3{font-family:'Montserrat',sans-serif;font-size:20px;font-weight:600}
  .step p{font-size:13px;line-height:1.4;margin-top:6px;color:var(--muted)}

  /* testimonials */
  .reviews{top:1960px;height:510px;background:var(--white);text-align:center}
  .reviews h2{font-family:'Montserrat',sans-serif;font-weight:700;font-size:48px;margin-top:80px;letter-spacing:1px}
  .review-row{position:absolute;left:0;top:210px;width:1200px;display:flex;justify-content:center;gap:60px}
  .review{width:300px}
  .stars{color:var(--navy);font-size:22px;letter-spacing:4px}
  .review h3{font-family:'Montserrat',sans-serif;font-weight:400;font-size:22px;margin-top:12px;letter-spacing:.5px}
  .review p{font-size:14px;line-height:1.45;color:var(--muted);margin-top:14px}
  .dots{position:absolute;left:0;top:416px;width:1200px;display:flex;justify-content:center;gap:8px}
  .dots span{width:10px;height:10px;border-radius:50%;background:#bfc3c8}
  .dots span.active{background:var(--navy)}

  /* confidence */
  .confidence{top:2470px;height:340px;background:var(--navy);color:var(--white)}
  .confidence h2{position:absolute;left:100px;top:100px;font-family:'Montserrat',sans-serif;font-weight:600;font-size:38px;line-height:1.2;width:480px}
  .confidence .btn{position:absolute;left:100px;top:210px;background:var(--black);color:var(--white);border-radius:2px;padding:15px 30px}
  .confidence-photo{position:absolute;left:620px;top:0;width:580px;height:340px;background:linear-gradient(120deg,#6e7c8c,#c8ced6 60%,#e6e8eb)}

  /* footer */
  .site-footer{top:2810px;height:486px;background:var(--black);color:var(--white)}
  .site-footer .brand{position:absolute;left:0;width:1200px;justify-content:center;top:56px;color:var(--white);font-size:52px}
  .site-footer .brand-dot{background:var(--white)}
  .footer-cols{position:absolute;left:210px;top:190px;display:flex;gap:150px}
  .footer-col h4{font-family:'Montserrat',sans-serif;font-size:28px;font-weight:600;margin-bottom:18px}
  .footer-col li{list-style:none;font-size:15px;line-height:1.75}
  .contact-line{display:flex;align-items:center;gap:12px}
  .contact-line svg{width:18px;height:18px;fill:var(--white)}
  .footer-rule{position:absolute;left:210px;top:430px;width:780px;border-top:1px solid #333}
  .copyright{position:absolute;left:0;top:448px;width:1200px;text-align:center;font-size:14px}
</style>
</head>
<body>

<header class="site-header">
  <div class="brand"><span class="brand-dot"></span>MPD</div>
  <nav class="nav">
    <span>Home</span><span>About Us</span><span>How We Work</span><span>Blog</span>
    <span class="btn">Contact Us</span>
  </nav>
</header>

<section class="hero">
  <div class="hero-photo" role="img" aria-label="Photo of two executives in a bright office reviewing a tablet together"></div>
  <div class="hero-panel">
    <h1>LEADERSHIP<br>ISN'T SHORT<br>ON STRATEGY</h1>
    <p>When pressure builds, someone has to carry the weight of delivery.</p>
    <span class="btn">Get Started!</span>
  </div>
</section>

<section class="outcome">
  <svg class="outcome-banner" viewBox="0 0 690 180" aria-hidden="true"><polygon points="0,0 620,0 690,90 620,180 0,180"/></svg>
  <h2>THE OUTCOME <strong>WE DELIVER</strong></h2>
  <div class="outcome-copy">
    <p>MPD helps Boards, CEO and Business Owners to: without the cost, permanence or complexity of a full-time executive hire.</p>
    <p>We do this by embedding as a trusted right-hand executive: accountable, practical, and focused on outcomes - not reports.</p>
  </div>
  <span class="btn">Read More</span>
  <svg class="outcome-photo" viewBox="0 0 480 550" role="img" aria-label="Photo of two businesswomen looking at a laptop, framed in a hexagon">
    <defs><linearGradient id="hexFill" x1="0" y1="0" x2="1" y2="1"><stop offset="0" stop-color="#d9dde2"/><stop offset="1" stop-color="#9aa6b3"/></linearGradient></defs>
    <polygon points="120,0 360,0 480,275 360,550 120,550 0,275" fill="#12314D"/>
    <polygon points="128,14 352,14 464,275 352,536 128,536 16,275" fill="url(#hexFill)"/>
  </svg>
</section>

<section class="how">
  <h2>HOW WE WORKS</h2>
  <p class="lead">This simple, repeatable model keeps engagements focused and outcome-driven</p>
  <div class="steps">
    <div class="step"><span class="step-num">01</span><h3>Diagnose</h3><p>Rapidly understand the real issues, risk and priorities.</p></div>
    <div class="step"><span class="step-num">02</span><h3>Embed</h3><p>Step inside the business as a trusted executive partner.</p></div>
    <div class="step"><span class="step-num">03</span><h3>Execute</h3><p>Drive delivery, decisions and implementation.</p></div>
    <div class="step"><span class="step-num">04</span><h3>Stabilise</h3><p>Restore rhythm, control and confidence.</p></div>
    <div class="step"><span class="step-num">05</span><h3>Transition</h3><p>Hand over cleanly to internal leaders or permanent roles</p></div>
  </div>
</section>

<section class="reviews">
  <h2>WHAT OUR CUSTOMERS SAYS</h2>
  <div class="review-row">
    <div class="review"><div class="stars">★★★★★</div><h3>MAECENAS FERMENTUM ELIT</h3><p>Etiam egestas fermentum ante, sed convallis orci tincidunt id. Lorem ipsum dolor sit amet, consectetur adipiscing elit</p></div>
    <div class="review"><div class="stars">★★★★★</div><h3>MAECENAS FERMENTUM ELIT</h3><p>Etiam egestas fermentum ante, sed convallis orci tincidunt id. Lorem ipsum dolor sit amet, consectetur adipiscing elit</p></div>
    <div class="review"><div class="stars">★★★★★</div><h3>MAECENAS FERMENTUM ELIT</h3><p>Etiam egestas fermentum ante, sed convallis orci tincidunt id. Lorem ipsum dolor sit amet, consectetur adipiscing elit</p></div>
  </div>
  <div class="dots"><span class="active"></span><span></span><span></span></div>
</section>

<section class="confidence">
  <h2>Financial, Tax &amp; Compliance Confidence</h2>
  <span class="btn">Schedule a Clarity Call</span>
  <div class="confidence-photo" role="img" aria-label="Photo of an advisor meeting with a senior couple at a desk"></div>
</section>

<footer class="site-footer">
  <div class="brand"><span class="brand-dot"></span>MPD</div>
  <div class="footer-cols">
    <div class="footer-col"><h4>Company</h4><ul><li>Home</li><li>About Us</li><li>How We Work</li><li>Blog</li><li>Contact Us</li></ul></div>
    <div class="footer-col"><h4>Value Proposition</h4><ul><li>Finance &amp; Commercial</li><li>Operation &amp; Execution</li><li>CEO/ Board Right-Hand Support</li><li>Risk, Governance &amp; Compliance</li><li>Clients Typical Engage Us</li></ul></div>
    <div class="footer-col"><h4>Contact</h4><ul>
      <li class="contact-line"><svg viewBox="0 0 24 24" aria-hidden="true"><path d="M6.6 10.8a15.1 15.1 0 0 0 6.6 6.6l2.2-2.2c.3-.3.7-.4 1-.2 1.1.4 2.3.6 3.6.6.6 0 1 .4 1 1V20c0 .6-.4 1-1 1A17 17 0 0 1 3 4c0-.6.4-1 1-1h3.5c.6 0 1 .4 1 1 0 1.3.2 2.5.6 3.6.1.3 0 .7-.2 1z"/></svg>0400 555 218</li>
      <li class="contact-line"><svg viewBox="0 0 24 24" aria-hidden="true"><path d="M3 5h18v14H3zM4.5 6.5v.3l7.5 5 7.5-5v-.3zm0 2v9h15v-9l-7.5 5z"/></svg>hello@mpdexecutive.com.au</li>
    </ul></div>
  </div>
  <div class="footer-rule"></div>
  <p class="copyright">Copyright 2026. All Rights Reserved | MPD</p>
</footer>

</body>
</html>
```